Velbrook Health is a Direct primary office that needs a great flyer design

Velbrook Health has been rebranded with a new logo and website and need new flyers to fit in with our new model and direction. Please refer to velbrook.example for content. Attached is a possible layout.

```html
<!DOCTYPE html>
<html lang="en">
<head>
<meta charset="utf-8">
<title>Velbrook Health – Direct Primary Care Flyer</title>
<link href="https://fonts.googleapis.com/css2?family=Raleway:wght@300;400;500;700;800&display=swap" rel="stylesheet">
<style>
  :root {
    --sky: #e4f2fb;
    --blue: #2f6db4;
    --navy: #0d3d6e;
    --green: #8dc35a;
    --light-blue: #8cc8ec;
    --white: #ffffff;
  }
  * { margin: 0; padding: 0; box-sizing: border-box; }
  html, body { width: 1200px; height: 928px; overflow: hidden; background: var(--white); }
  body { font-family: "Raleway", sans-serif; }
  .flyer { position: relative; width: 1200px; height: 928px; overflow: hidden; background: var(--white); }

  .panel-left { position: absolute; left: 0; top: 0; width: 400px; height: 928px;
    background: linear-gradient(160deg, #e2f1fb 0%, #d3e8f7 60%, #c6e0f3 100%); }
  .panel-right { position: absolute; left: 800px; top: 0; width: 400px; height: 928px; background: var(--sky); }

  .shapes { position: absolute; left: 0; top: 0; width: 1200px; height: 928px; }

  .hero-title { position: absolute; right: 835px; top: 42px; text-align: right; }
  .hero-title .lead { color: var(--green); font-weight: 800; font-size: 25px; line-height: 27px; }
  .hero-title .sub { color: var(--navy); font-weight: 300; font-size: 26px; line-height: 26px; }
  .hero-title .promise { margin-top: 8px; color: var(--navy); font-weight: 800; font-size: 18.5px; line-height: 22px; }

  .invest-badge { position: absolute; left: 271px; top: 416px; width: 94px; height: 94px; border-radius: 50%;
    background: var(--green); color: var(--white); font-weight: 800; font-size: 16px; line-height: 20px;
    display: flex; align-items: center; justify-content: center; text-align: center; }

  .dpc-intro { position: absolute; left: 44px; top: 482px; width: 322px; color: var(--white); }
  .dpc-intro h2 { color: var(--light-blue); font-weight: 700; font-size: 22px; margin-bottom: 10px; }
  .dpc-intro p { font-size: 14.4px; line-height: 16.4px; font-weight: 500; }

  .about { position: absolute; left: 440px; top: 56px; width: 320px; color: var(--blue); }
  .about h2 { font-size: 29px; font-weight: 300; line-height: 34px; margin-bottom: 14px; }
  .about h2 strong { font-weight: 800; }
  .about p { font-size: 13.2px; line-height: 16.8px; margin-bottom: 12px; }

  .highlights { position: absolute; right: 441px; top: 446px; text-align: right; list-style: none;
    color: var(--green); font-weight: 700; font-size: 17px; }
  .highlights li { height: 33.5px; }

  .faq { position: absolute; left: 841px; top: 56px; width: 320px; color: var(--blue); }
  .faq h2 { font-size: 29px; font-weight: 300; line-height: 34px; margin-left: 5px; margin-bottom: 14px; }
  .faq h3 { color: var(--navy); font-weight: 800; font-size: 16.5px; line-height: 18px;
    padding-bottom: 5px; border-bottom: 1.5px solid var(--navy); margin-bottom: 6px; }
  .faq p { font-size: 13.2px; line-height: 16.7px; margin-bottom: 14px; }
  .faq p.tight { margin-bottom: 8px; }
  .faq .gap { margin-bottom: 24px; }
  .nowrap { white-space: nowrap; }
</style>
</head>
<body>
<div class="flyer">
  <div class="panel-left"></div>
  <div class="panel-right"></div>

  <svg class="shapes" viewBox="0 0 1200 928">
    <defs>
      <linearGradient id="waveFill" x1="0" y1="0" x2="0.3" y2="1">
        <stop offset="0" stop-color="#0f6aa8"/>
        <stop offset="0.55" stop-color="#1a78ac"/>
        <stop offset="1" stop-color="#6aae8a"/>
      </linearGradient>
      <linearGradient id="photoFill" x1="0" y1="0" x2="1" y2="1">
        <stop offset="0" stop-color="#dfe9ee"/>
        <stop offset="1" stop-color="#9fb7c4"/>
      </linearGradient>
    </defs>

    <rect x="20" y="222" width="250" height="238" rx="6" fill="#c9dfee" role="img"
      aria-label="Photo: smiling doctor with clipboard beside a mother and daughter"/>

    <path d="M0,462 C150,438 330,468 430,560 C540,660 620,780 663,928 L0,928 Z" fill="url(#waveFill)"/>

    <path d="M0,760 C80,724 220,718 300,760 C340,800 365,870 378,928 L0,928 Z" fill="url(#photoFill)"
      role="img" aria-label="Photo: doctor reviewing a clipboard with a patient beside medical equipment"/>

    <circle cx="600" cy="729" r="112" fill="#c9a58f" role="img"
      aria-label="Photo: multi-generation family laughing together at home"/>
  </svg>

  <div class="hero-title">
    <div class="lead">Direct Primary Care</div>
    <div class="sub">Benefits Patients</div>
    <div class="sub">By Providing</div>
    <div class="promise">SUBSTANTIAL SAVINGS<br>&amp; A GREATER DEGREE OF ACCESS<br>TO YOUR DOCTOR.</div>
  </div>

  <div class="invest-badge">Invest in<br>Your<br>Health</div>

  <section class="dpc-intro">
    <h2>Direct Primary Care</h2>
    <p>The direct primary care (DPC) model gives patients a meaningful alternative to the insurance driven medical community by charging patients a monthly fee that covers all primary care services including clinical, wellness consultative services, care coordination and comprehensive care management. Labs are provided at a significantly reduced price. Because some services are not covered by the monthly fee, DPC practices often suggest that patients acquire a high-deductible wraparound policy to cover emergencies and specialist care.</p>
  </section>

  <section class="about">
    <h2>About <strong>Us</strong></h2>
    <p>Our mission is to provide patient-centered care that is respectful, honest and compassionate.</p>
    <p>Our goal is to make a significant impact on the lives of people in the surrounding communities through health education, better care and disease prevention.</p>
    <p>We believe that health care should revolve around decisions that patients make between themselves and their doctor, not what the insurance-controlled model dictates because of cost, time or convenience. As a Direct Primary Care provider, we focus on you and your health without the interference of outside interests. Our model allows more time with you, 24/7 access to your provider, which we believe is critical to developing relationships and making appropriate decisions for wellness, medical care and chronic care management.</p>
  </section>

  <ul class="highlights">
    <li>Satisfied patients</li>
    <li>State of the art facility</li>
    <li>A world-class team of professionals</li>
  </ul>

  <section class="faq">
    <h2>FAQ</h2>
    <h3>What is direct primary care?</h3>
    <p class="gap">Direct primary care is an affordable alternative approach to health care and medical services. Instead of dealing with costly co-pays and insurance claim forms, and waiting to get reimbursed, DPC allows you to pay a monthly, quarterly, or annual fee to the health care provider of your choice. In return for this “membership” or “retainer” fee, you have access to your medical practitioner whenever you need them.</p>
    <h3>How is a direct primary care practice different?</h3>
    <p class="tight">One of the biggest differences between DPC practices and traditional practices is that in a DPC practice, you’ll have access to your health care provider at your convenience. Visits to the office for medical exams, routine physicals, lab work, or other comprehensive health and wellness services are unlimited, so you don’t have to worry about an expensive co-pay each time you make an appointment. Your physician is there when you need them most, so you can maintain good health, get medical attention for an illness, or learn how to better manage a chronic condition.</p>
    <p class="gap">Velbrook Health offers DPC for its numerous advantages, one of which is spending more time with your health care provider at each visit. We believe in taking our time with each individual, typically 30-45 minutes per visit, so we can develop a therapeutic relationship to best serve your health care needs.</p>
    <h3>Is Direct Primary Care and Concierge Medicine the same?</h3>
    <p>No. Concierge Medicine may charge insurance,<br><span class="nowrap">co-pays</span> and co-insurance along concierge fees to pay for services. Direct Primary Care only accepts membership fees or same day payments for services.</p>
  </section>
</div>
</body>
</html>
```